Technology Solutions Provider

Let’s design a business card that will be as simple and bold at the same time. Name, email address, website & phone number.

Target Market(s)

Small to Medium Size Business

Industry/Entity Type

It Professional

Contact Information for Business Card

Name, email, website, phone numbers

Font styles to use
Sans Serif

Colors
ec1f27
f04a50
dddddd
919191
000000
ffffff

Requirements
Must have
• Clean simple look using my existing logo. I just need to the basic contact information on this card.
Nice to have
• Im considering the square size card versus the standard size business card.
Should not have
• No Mailing Address, no list of services.

```html
<!DOCTYPE html>
<html lang="en">
<head>
<meta charset="utf-8">
<title>Kestrel Systems — Business Card</title>
<link rel="stylesheet" href="https://fonts.googleapis.com/css2?family=Montserrat:wght@500;600&display=swap">
<style>
  :root {
    --red: #ec1f27;
    --red-soft: #f04a50;
    --light-grey: #dddddd;
    --mid-grey: #919191;
    --black: #000000;
    --white: #ffffff;
    --icon-green: #3aa43a;
    --stage: #e9e9e9;
  }
  * { box-sizing: border-box; margin: 0; padding: 0; }
  html, body { width: 1200px; height: 780px; overflow: hidden; }
  body {
    background: var(--stage);
    font-family: "Montserrat", sans-serif;
    position: relative;
  }
  .card {
    position: absolute;
    top: 242px;
    width: 525px;
    height: 300px;
    box-shadow: 0 6px 18px rgba(0,0,0,0.18);
    overflow: hidden;
  }
  .card--front { left: 45px; background: var(--white); }
  .card--back { left: 630px; background: var(--black); }

  .brand {
    position: absolute;
    display: flex;
    align-items: center;
    gap: 10px;
  }
  .brand__mark {
    width: 14px; height: 14px; border-radius: 50%;
    background: var(--red);
    flex: none;
  }
  .brand__name {
    font-size: 28px;
    font-weight: 600;
    line-height: 1;
    white-space: nowrap;
  }
  .card--front .brand { left: 120px; top: 88px; }
  .card--front .brand__name { color: var(--black); }
  .card--back .brand { left: 120px; top: 133px; }
  .card--back .brand__name { color: var(--white); }

  .holder {
    position: absolute;
    right: 290px;
    top: 172px;
    text-align: right;
    white-space: nowrap;
  }
  .holder__name { font-size: 13px; font-weight: 600; color: var(--black); }
  .holder__role { font-size: 10.5px; font-weight: 500; color: var(--red); margin-top: 4px; }

  .divider {
    position: absolute;
    left: 247px; top: 164px;
    width: 1.5px; height: 50px;
    background: var(--mid-grey);
  }

  .contacts {
    position: absolute;
    left: 260px; top: 162px;
    list-style: none;
  }
  .contacts__item {
    display: flex; align-items: center; gap: 8px;
    font-size: 10.5px; font-weight: 500; color: var(--black);
    height: 18px; white-space: nowrap;
  }
  .contacts__icon { width: 11px; height: 11px; flex: none; }

  .rule {
    position: absolute;
    height: 3px;
    background: var(--red);
  }
  .rule--upper { left: 190px; right: 0; top: 228px; }
  .rule--lower { left: 0; right: 0; top: 278px; }
</style>
</head>
<body>

<section class="card card--front" aria-label="Business card front">
  <div class="brand">
    <span class="brand__mark"></span>
    <span class="brand__name">Kestrel Systems</span>
  </div>

  <div class="holder">
    <p class="holder__name">Daniel Hartwell</p>
    <p class="holder__role">Managing Director</p>
  </div>

  <span class="divider"></span>

  <ul class="contacts">
    <li class="contacts__item">
      <svg class="contacts__icon" viewBox="0 0 12 12" aria-hidden="true">
        <path d="M1 4c0-2 1-3 2-3l1.5 2.5L3.5 5c.8 1.6 1.9 2.7 3.5 3.5l1.5-1L11 9c0 1-1 2-3 2C4 11 1 8 1 4z" fill="var(--icon-green)"/>
      </svg>
      555.014.2760
    </li>
    <li class="contacts__item">
      <svg class="contacts__icon" viewBox="0 0 12 12" aria-hidden="true">
        <rect x="0.5" y="2" width="11" height="8" fill="var(--icon-green)"/>
        <path d="M0.5 2L6 7l5.5-5" fill="none" stroke="#ffffff" stroke-width="1"/>
      </svg>
      hello@kestrelsys.com
    </li>
    <li class="contacts__item">
      <svg class="contacts__icon" viewBox="0 0 12 12" aria-hidden="true">
        <circle cx="6" cy="6" r="5.5" fill="var(--icon-green)"/>
        <path d="M0.5 6h11M6 0.5c-2.5 3-2.5 8 0 11M6 0.5c2.5 3 2.5 8 0 11" fill="none" stroke="#ffffff" stroke-width="0.8"/>
      </svg>
      www.kestrelsys.com
    </li>
  </ul>

  <span class="rule rule--upper"></span>
  <span class="rule rule--lower"></span>
</section>

<section class="card card--back" aria-label="Business card back">
  <div class="brand">
    <span class="brand__mark"></span>
    <span class="brand__name">Kestrel Systems</span>
  </div>
</section>

</body>
</html>
```